Newsletter for a recent surgical mission conducted by Bright Shores Relief

We need a one page, two sided newsletter reporting the events of our recent mission trip. The first page should have the title Bright Shores Relief along with the mission date of November 2019 and Cayo, Belize as the location. We want to highlight the pictures of the children especially the before and after pictures. Pictures of the hospital and ward should give the viewer the feel that they visited the hospital with us and to show how basic and rustic it is. Maybe stock photos of mountainous green landscape would help.

Target Market(s)

Our donors receive this and we want to highlight what we did and how their contributions enabled us to do it.

Industry/Entity Type

Non Profit

Font styles to use
Sans Serif

Colors

Designer to choose colors to be used in the design.

Requirements
Must have
• 1. The organization logo
• 2. Please match the text describing each patient to the corresponding pictures of the patients.
• 3. Highlighted text thanking our donors for donating.
• 4. www.brightshoresrelief should be included which is our website.
• 5. Text asking anyone who wants to contribute to our next mission to visit the Donate link on our website.
Nice to have
• 1. Stock images of the Belizean landscape can be used along with the picture of the hospital.
• 2. I am not sure what 'GREYSCALE" is but it might be interesting to see what a version of the newsletter looks like in that color. We have always matched the colors in the logo. If not, then just match the colors in the logo but let the designer choose.
Should not have
• When including the picture of us the surgeons, keep it small. We want to highlight the patients NOT the staff.

```html
<!DOCTYPE html>
<html lang="en">
<head>
<meta charset="utf-8">
<title>Bright Shores Relief – Mission Newsletter</title>
<link rel="stylesheet" href="https://fonts.googleapis.com/css2?family=Abel&family=Oswald:wght@300;400&family=PT+Sans:wght@400;700&display=swap">
<style>
  :root {
    --page: #ffffff;
    --green: #3f8f3a;
    --teal: #3f8b86;
    --blue: #4d86cf;
    --text-light: #ffffff;
    --text-dark: #111111;
    --brand: #3f8b86;
    --photo-warm: #c9a58a;
    --photo-cool: #8fb2c4;
    --photo-green: #6f9a86;
    --photo-blue: #6e8fb8;
  }
  * { box-sizing: border-box; margin: 0; padding: 0; }
  html, body { width: 877px; height: 1200px; overflow: hidden; background: var(--page); }
  .newsletter {
    position: relative;
    width: 877px;
    height: 1200px;
    background: var(--page);
    font-family: "PT Sans", sans-serif;
    color: var(--text-light);
  }
  .masthead {
    position: absolute;
    left: 49px; top: 8px;
    width: 782px; height: 30px;
    display: flex; align-items: center; justify-content: space-between;
    font-family: "PT Sans", sans-serif;
    color: var(--text-dark);
  }
  .brand {
    display: flex; align-items: center; gap: 9px;
  }
  .brand__mark {
    width: 18px; height: 18px; border-radius: 50%;
    background: var(--brand);
  }
  .brand__name {
    font-size: 22px; font-weight: 700; line-height: 30px;
    color: var(--brand);
  }
  .mission-info {
    font-size: 17px; line-height: 30px;
  }
  .panel {
    position: absolute;
    left: 49px; top: 44px;
    width: 782px; height: 1114px;
    background: linear-gradient(200deg, var(--green) 0%, var(--teal) 45%, var(--blue) 100%);
  }
  .photo {
    position: absolute;
    border-radius: 18px;
    overflow: hidden;
  }
  .story {
    position: absolute;
    font-size: 18.6px;
    line-height: 25.6px;
    text-align: justify;
    hyphens: auto;
  }
  .story--column { font-size: 17.2px; line-height: 25.5px; }
  .story--wide { font-size: 15.4px; line-height: 20.7px; }
  .rule {
    position: absolute;
    height: 2px;
    background: var(--text-light);
  }
  .staff-title {
    position: absolute;
    left: 66px; top: 327px; width: 362px;
    text-align: center;
    font-family: "Abel", sans-serif;
    font-weight: 400;
    font-size: 47px;
    line-height: 56px;
  }
  .thanks {
    position: absolute;
    left: 70px; top: 676px; width: 350px;
    text-align: center;
  }
  .thanks__lead {
    font-family: "Abel", sans-serif;
    font-size: 62px;
    line-height: 72px;
    color: var(--text-light);
  }
  .thanks__word {
    font-family: "Oswald", sans-serif;
    font-weight: 400;
    font-size: 90px;
    line-height: 100px;
    color: var(--text-dark);
    letter-spacing: 0.5px;
  }
  .cta {
    position: absolute;
    left: 66px; top: 1079px;
    width: 748px; height: 58px;
    background: var(--page);
    color: var(--text-dark);
    display: flex; align-items: center; justify-content: center;
    gap: 14px;
    white-space: nowrap;
  }
  .cta__lead {
    font-family: "Oswald", sans-serif;
    font-weight: 300;
    font-size: 34px;
    letter-spacing: -0.5px;
  }
  .cta__url {
    font-family: "Abel", sans-serif;
    font-size: 36px;
  }
  .family-frame {
    position: absolute;
    left: 530px; top: 881px;
    width: 281px; height: 187px;
    border-radius: 18px;
    background: var(--page);
    overflow: hidden;
  }
</style>
</head>
<body>
<main class="newsletter">
  <header class="masthead">
    <div class="brand">
      <span class="brand__mark"></span>
      <h1 class="brand__name">Bright Shores Relief</h1>
    </div>
    <p class="mission-info">Surgical Mission · Cayo, Belize · November 2019</p>
  </header>

  <div class="panel"></div>

  <div class="photo" style="left:66px;top:73px;width:297px;height:233px;background:linear-gradient(120deg,#e9ece6 0%,var(--photo-cool) 55%,#3b5fa8 100%);" role="img" aria-label="Photo of the patient seated on a hospital bed beside a surgeon in scrubs"></div>

  <p class="story" style="left:381px;top:52px;width:447px;">This is Marco Reyes, a 23 year old man from the town of Santa Elena in Cayo. He sustained a left upper arm injury from a rotating saw four years ago that lacerated his radial nerve. It was never repaired and now he cannot extend his wrist, thumb and fingers. The Team performed forearm muscle and tendon transfers which after a 6-week recovery will allow him to get back to work doing construction.</p>

  <div class="rule" style="left:66px;top:320px;width:359px;"></div>
  <h2 class="staff-title">Our staff</h2>

  <div class="photo" style="left:73px;top:392px;width:175px;height:245px;background:linear-gradient(160deg,#d8e4e2 0%,var(--photo-green) 45%,#2e5d5a 100%);" role="img" aria-label="Photo of the surgical team operating in the theatre"></div>
  <div class="photo" style="left:253px;top:392px;width:175px;height:245px;background:linear-gradient(170deg,#f1f1ef 0%,var(--photo-blue) 55%,#2c4f8a 100%);" role="img" aria-label="Photo of the surgeons posing together in scrubs"></div>

  <div class="rule" style="left:79px;top:666px;width:340px;"></div>
  <div class="rule" style="left:79px;top:675px;width:340px;"></div>
  <div class="thanks">
    <div class="thanks__lead">Thanks for</div>
    <div class="thanks__word">DONATION</div>
  </div>
  <div class="rule" style="left:79px;top:871px;width:340px;"></div>
  <div class="rule" style="left:79px;top:880px;width:340px;"></div>

  <div class="photo" style="left:438px;top:320px;width:173px;height:220px;background:linear-gradient(160deg,#b98c6d 0%,var(--photo-warm) 50%,#4a4a55 100%);" role="img" aria-label="Photo of a baby boy with a cleft lip"></div>
  <div class="photo" style="left:624px;top:320px;width:185px;height:220px;background:linear-gradient(160deg,#d97a9a 0%,#8a5c4a 50%,#e3e6ea 100%);" role="img" aria-label="Photo of a baby girl with a cleft lip"></div>

  <p class="story story--column" style="left:438px;top:549px;width:175px;">This is Tavi Chan and his mother, Lorena. Tavi is 7 months old and was born with a severe cleft lip. His mom brought him to see us and the Team was able to repair his cleft lip this week before they head back to their home in Stann Creek, Cayo.</p>

  <p class="story story--column" style="left:624px;top:549px;width:186px;">This is Nia Pascal from the small town of Spanish Lookout in Cayo, Belize. Nia is 5 months old and was born with a cleft lip and palate. The Team was able to help her by performing the 1st of 4 surgeries she will need to reconstruct her lip, palate and nose.</p>

  <div class="rule" style="left:436px;top:869px;width:378px;"></div>

  <p class="story story--wide" style="left:66px;top:884px;width:450px;">This is 5 year old Elian Ruiz with his Mom and Dad. They are from the Frank’s Eddy Village in Belize. Elian had his cleft lip and palate repaired when he was younger. Unfortunately, he developed an opening in the roof of his mouth afterwards (palatal fistula) that results in liquid and food in his mouth coming out his nose when he ate. The Team was able to repair his palate this week and in a short time get back to eating normally.</p>

  <div class="family-frame">
    <div style="position:absolute;left:0;top:0;width:136px;height:187px;border-radius:18px;background:linear-gradient(160deg,#7fb0d6 0%,#c7a088 55%,#5a8fbf 100%);" role="img" aria-label="Photo of the boy in a surgical cap after his palate repair"></div>
    <div style="position:absolute;left:142px;top:0;width:139px;height:187px;border-radius:18px;background:linear-gradient(160deg,#e9e4dc 0%,#d0708e 45%,#3e5a8a 100%);" role="img" aria-label="Photo of the boy with his mother and father"></div>
  </div>

  <div class="cta">
    <span class="cta__lead">To Contribute please visit:</span>
    <span class="cta__url">www.brightshoresrelief.com</span>
  </div>
</main>
</body>
</html>
```